Higher $ Now Guaranteed! Redesign Web Page(s) Style Composition and Color (Graphics design-not code)

We need a modern look for an existing website. You can either use or change the current logo. Choice of colors, fonts, style is up to you. Sample URLs and additional details are provided in the attached document. Most of our struggle has been the appearance of the directory listings (city) page.
----------------------------------------------------------------------------------
--> Increased Project Budget and Now Funds are GUARANTEED
--> Added an additional attachment in response to questions
-->THIS PROJECT IS FOR GRAPHICS/DESIGN NOT CODE
The project is mostly a few areas of text and colored boxes or lines. Hopefully a skilled designer can place these elements in an attractive layout and choose the right colors and styles. There are no complex drawings required for this project.

*** We are involved with other projects from time to time and expect that the winning designer will be given the first opportunity at this future work. ***

*** There is no requirement to do any code but if you submit a design feel free to indicate if you wish to be considered for any future code work on this site or others ***

Font styles to use
Sans Serif

Requirements
Must have
• Rounded corners on images and buttons with nice gradients or hover effects.
Nice to have
• Attached an additional descriptions document to help with these answers.
Should not have
• Small fonts, traditional older looking rectangular buttons, dull or boring color schemes

```html
<!DOCTYPE html>
<html lang="en">
<head>
<meta charset="utf-8">
<title>TaxFinderHub – Tax Preparer Directory</title>
<link href="https://fonts.googleapis.com/css2?family=PT+Sans:wght@400;700&display=swap" rel="stylesheet">
<style>
  :root{
    --ink:#2b3a44;
    --slate:#3f6273;
    --cyan:#0ab0d1;
    --amber:#f6b836;
    --amber-dark:#e6a51f;
    --rose:#e04a58;
    --rose-dark:#c93a48;
    --leaf:#7ab442;
    --leaf-dark:#659a33;
    --grey-text:#9a9fa3;
    --panel-line:#e4e6e8;
    --footer:#21404f;
    --footer-head:#8ba0ab;
    --white:#ffffff;
    --page:#f4f5f6;
  }
  *{box-sizing:border-box;margin:0;padding:0}
  html,body{width:1200px;height:778px;overflow:hidden}
  body{
    font-family:"PT Sans",Arial,sans-serif;
    color:var(--ink);
    background:
      repeating-linear-gradient(45deg,rgba(0,0,0,.025) 0 1px,transparent 1px 8px),
      repeating-linear-gradient(-45deg,rgba(0,0,0,.025) 0 1px,transparent 1px 8px),
      var(--page);
    position:relative;
  }
  .site-header{position:absolute;left:0;top:0;width:1200px;height:105px;background:var(--white)}
  .brand{position:absolute;left:74px;top:34px;display:flex;align-items:center;gap:8px;
    font-size:24px;font-weight:700;color:var(--slate)}
  .brand-dot{width:14px;height:14px;border-radius:50%;background:var(--slate)}
  .main-nav{position:absolute;left:607px;top:0;display:flex;gap:48px}
  .main-nav a{display:block;padding-top:43px;font-size:15px;color:var(--ink);text-decoration:none;letter-spacing:.3px;position:relative}
  .main-nav a.is-active::before{content:"";position:absolute;left:-13px;right:-13px;top:0;height:7px;background:var(--slate)}
  .phone{position:absolute;left:936px;top:34px;display:flex;align-items:center;gap:12px;
    font-size:23px;font-weight:700;color:var(--slate)}
  .search-band{position:absolute;left:74px;top:105px;width:1052px;height:74px;background:var(--cyan);
    border-radius:0 0 6px 6px;display:flex;align-items:center;padding-left:27px}
  .search-label{color:var(--white);font-weight:700;font-size:16px;width:156px}
  .search-field{width:231px;height:37px;margin-right:18px;background:var(--white);border:none;
    padding:0 13px;font:14px "PT Sans",sans-serif;color:#b4b8bb;display:flex;align-items:center}
  .search-btn{width:111px;height:37px;margin-left:1px;border-radius:3px;
    background:linear-gradient(var(--amber),var(--amber-dark));color:var(--white);
    font-weight:700;font-size:14px;display:flex;align-items:center;justify-content:center;gap:8px}
  .map-hint{position:absolute;left:333px;top:204px;width:257px;height:27px;border-radius:4px;
    background:var(--amber);color:var(--white);font-weight:700;font-size:13.5px;
    display:flex;align-items:center;justify-content:center;box-shadow:0 2px 0 var(--amber-dark)}
  .map-hint::after{content:"";position:absolute;left:126px;bottom:-6px;border:6px solid transparent;border-bottom:0;border-top-color:var(--amber)}
  .us-map{position:absolute;left:74px;top:249px;width:600px;height:343px;border-radius:28px 60px 90px 40px;
    background:linear-gradient(135deg,#7fb0ea 0%,#8fd4dc 35%,#95a9b3 65%,#74a7e6 100%);opacity:.9}
  .cta-photo{position:absolute;left:777px;top:196px;width:284px;height:100px;border-radius:50px 50px 8px 8px;
    background:linear-gradient(180deg,#6b4a3a 0%,#d9b8a4 55%,#f1ddd0 100%)}
  .cta-panel{position:absolute;left:711px;top:292px;width:415px;height:306px;background:var(--white);
    border:1px solid var(--panel-line);border-radius:4px;box-shadow:0 3px 0 #e1e3e5;text-align:center}
  .cta-block{padding-top:20px}
  .cta-block + .cta-block{border-top:1px solid var(--panel-line);margin:0 18px;padding-top:14px}
  .cta-title{font-size:16.5px;font-weight:700;text-transform:uppercase}
  .cta-title.rose{color:var(--rose)}
  .cta-title.leaf{color:var(--leaf)}
  .cta-copy{margin-top:5px;font-size:12.5px;line-height:16px;color:var(--grey-text)}
  .cta-btn{display:inline-block;width:173px;height:40px;line-height:40px;margin:10px 0 18px;border-radius:4px;
    color:var(--white);font-weight:700;font-size:17px;letter-spacing:1px;text-transform:uppercase}
  .cta-btn.rose{background:linear-gradient(var(--rose),var(--rose-dark))}
  .cta-btn.leaf{background:linear-gradient(var(--leaf),var(--leaf-dark))}
  .site-footer{position:absolute;left:0;top:636px;width:1200px;height:142px;background:var(--footer);color:var(--white)}
  .footer-col{position:absolute;top:23px;font-size:12px;line-height:21px}
  .footer-col h4{font-size:13px;letter-spacing:1px;color:var(--footer-head);margin-bottom:5px}
  .footer-col a{color:var(--white);text-decoration:none;display:block}
  .footer-col a.is-hover{text-decoration:underline}
  .footer-brand{position:absolute;right:74px;top:50px;display:flex;align-items:center;gap:8px;font-size:22px;font-weight:700}
  .footer-brand .brand-dot{background:var(--white)}
</style>
</head>
<body>
  <header class="site-header">
    <div class="brand"><span class="brand-dot"></span>TaxFinderHub</div>
    <nav class="main-nav">
      <a href="#" class="is-active">HOME</a>
      <a href="#">GET LISTED</a>
      <a href="#">CONTACT US</a>
    </nav>
    <div class="phone">
      <svg width="36" height="36" viewBox="0 0 36 36" fill="none" stroke="#2b3a44" stroke-width="2.6" stroke-linecap="round">
        <path d="M9 5l5 6-3 3c1.5 4 5 7.5 9 9l3-3 6 5-3 5C15 30 5 20 4 9z"/>
        <path d="M21 9a7 7 0 0 1 6 6"/><path d="M22 3a13 13 0 0 1 11 11"/>
      </svg>
      555-014-2290
    </div>
  </header>

  <section class="search-band">
    <span class="search-label">FInd tax experts by</span>
    <span class="search-field">City</span>
    <span class="search-field">State</span>
    <span class="search-field">ZIP</span>
    <span class="search-btn">SEARCH
      <svg width="15" height="15" viewBox="0 0 16 16" fill="none" stroke="#fff" stroke-width="2"><circle cx="9" cy="7" r="5"/><path d="M5.5 10.5L2 14"/></svg>
    </span>
  </section>

  <div class="map-hint">Click on your location to get started</div>
  <div class="us-map" role="img" aria-label="Clickable map of the United States with each state labelled"></div>

  <div class="cta-photo" role="img" aria-label="Smiling woman leaning over the top of the panel"></div>
  <aside class="cta-panel">
    <div class="cta-block">
      <h2 class="cta-title rose">Are you tax preparer?</h2>
      <p class="cta-copy">Our directories of tax professionals give you immediate access<br>to the very best tax preparers and income tax advisors in your area.</p>
      <span class="cta-btn rose">Submit listing</span>
    </div>
    <div class="cta-block">
      <h2 class="cta-title leaf">Have a local tax firm contact me</h2>
      <p class="cta-copy">Our directories of tax professionals give you immediate access<br>to the very best tax preparers and income tax advisors in your area.</p>
      <span class="cta-btn leaf">Get started</span>
    </div>
  </aside>

  <footer class="site-footer">
    <div class="footer-col" style="left:74px">
      <h4>NAVIGATION</h4>
      <a href="#">Directory</a>
      <a href="#" class="is-hover">Special Offers</a>
      <a href="#">Contact Us</a>
    </div>
    <div class="footer-col" style="left:254px">
      <h4>CONTACT</h4>
      <span>PO Box 4410</span><br>
      <span>Millbrook, CT</span><br>
      <span>06999</span>
    </div>
    <div class="footer-col" style="left:434px">
      <h4>LEGAL</h4>
      <span>Lumen Ads © 2015</span><br>
      <span>website design</span><br>
      <span>by brightforgestudio.com</span>
    </div>
    <div class="footer-brand"><span class="brand-dot"></span>TaxFinderHub</div>
  </footer>
</body>
</html>
```